Beautify our company's one pager website

We need a website - currently we have only a nice light-switcher: https://brindlequay.example

We got the basic contents together (see the wireframes - also in SVG format -
attached here). Now we need you (!) to make it look appealing, create proper illustrations, provide a good theme picture and advice us on how to take good employee pictures.

In the wireframes, the picture and most illustrations are just placeholders (only the logos of "Our Open Source tools" are ours - see attached logos.svg). We request you to fill all placeholders with good illustrations and make the whole page look nicely.

Only one color is pre-defined (#11233f - the blue color we use for our logo when it is on white background). Feel free to give it nice colours based on your professional expertise and intuition. Feel also free to use the blue in a more creative way, than proposed in the wireframes.

We will do the coding ourselves, but we request you to submit a responsive design, with at least one version for mobiles, one for tablet size and one for full desktop resolution.

We think our people pictures should follow a design line. Please asses us on how we should take our colleagues' pictures (e.g. completely white background, or... blurry city background, or.... with a big box in the hand, etc... we are curious to see your suggestion).

In case of any doubts, please don't hesitate to contact us (brindlequay-website-design@brindlequay.example).

Target Market(s)

International cooperation agencies

Industry/Entity Type

Consulting

Number of Pages Required

Font styles to use
Other font styles liked:
• Lato

Colors

Designer to choose colors to be used in the design.

Requirements
Must have
• Responsive design in mind (one pager, for three different resolutions: mobile, tablet, desktop)
• Illustrations and (maybe) a photo - must be royalty-free and open for any use in the future.
Nice to have
• SVG formated design
• Suggestions on the peoples' photos

```html
<!DOCTYPE html>
<html lang="en">
<head>
<meta charset="utf-8">
<title>Brindle Quay – Agile Consultancies</title>
<link rel="stylesheet" href="https://fonts.googleapis.com/css2?family=Poppins:wght@300;400;500;600;700&family=Playfair+Display:ital,wght@1,700&display=swap">
<style>
:root{
  --navy:#11233f;
  --navy-deep:#0b1a31;
  --orange:#f28a1b;
  --grey-band:#8b8b8b;
  --ink:#1f2533;
  --muted:#555b66;
  --white:#ffffff;
}
*{box-sizing:border-box;margin:0;padding:0}
html,body{width:1200px;height:4849px;overflow:hidden}
body{font-family:"Poppins",sans-serif;color:var(--ink);background:var(--white);position:relative}
.abs{position:absolute}
.btn{display:inline-block;background:var(--orange);color:var(--white);font-weight:600;font-size:12px;letter-spacing:.5px;padding:11px 20px;text-transform:uppercase}
.section-title{font-weight:700;font-size:34px;text-align:center;color:var(--navy);width:100%}
.section-title::after{content:"";display:block;width:92px;height:5px;background:var(--orange);margin:12px auto 0}
.serif{font-family:"Playfair Display",serif;font-style:italic;font-weight:700}

/* hero */
.hero{left:0;top:0;width:1200px;height:745px;background:linear-gradient(120deg,#1a2b48 0%,#2a3b55 45%,#51606f 100%)}
.hero-photo{left:560px;top:0;width:640px;height:745px;background:radial-gradient(ellipse at 55% 55%,rgba(120,140,110,.55) 0%,rgba(60,80,100,.25) 45%,rgba(0,0,0,0) 75%)}
.brand{left:188px;top:52px;color:var(--white);font-weight:700;font-size:30px;letter-spacing:1px}
.nav{left:550px;top:64px;display:flex;gap:44px;font-size:14px;font-weight:500;letter-spacing:1px;color:var(--white)}
.nav .active{color:var(--orange)}
.hero-title{left:188px;top:250px;color:var(--white)}
.hero-title .serif{font-size:82px;line-height:1}
.hero-title .big{font-size:62px;font-weight:700;line-height:1.05}
.hero-title .sub{font-size:26px;font-weight:700;margin-top:10px}
.hero .btn{position:absolute;left:188px;top:472px}
.arrow{top:350px}

/* about */
.about-photo{left:130px;top:834px;width:420px;height:282px;background:linear-gradient(135deg,#d7dbe0,#7d8896 60%,#3f4b5a)}
.about-text{left:647px;top:842px;width:440px;font-size:13.5px;line-height:2;color:var(--muted)}
.about-btn{left:647px;top:1066px}

/* agile band */
.agile{left:0;top:1197px;width:1200px;height:307px;background:var(--grey-band);color:var(--white)}
.agile .serif{position:absolute;left:188px;top:30px;font-size:96px}
.agile p{position:absolute;left:188px;top:148px;width:860px;font-size:18px;line-height:1.7}

/* services */
.services-title{left:0;top:1585px}
.service{top:1680px;width:300px;text-align:center}
.service .icon{width:124px;height:124px;border-radius:50%;background:var(--orange);margin:0 auto;display:flex;align-items:center;justify-content:center;box-shadow:0 0 0 5px var(--white),0 0 0 8px var(--orange)}
.service h3{margin-top:38px;font-size:20px;font-weight:700;color:var(--navy);line-height:1.3}
.service p{margin-top:14px;font-size:13.5px;line-height:1.75;color:var(--muted)}

/* tools */
.tools{left:0;top:2086px;width:1200px;height:454px;background:linear-gradient(120deg,#3f4247,#2f3135 55%,#45484d)}
.tools .section-title{color:var(--white);position:absolute;top:112px}
.tool{top:2262px;width:440px;color:var(--white)}
.tool .head{display:flex;align-items:center;gap:14px;margin-left:80px;font-size:26px;font-weight:700;color:var(--orange)}
.tool p{margin-top:18px;font-size:13px;line-height:2;color:#e2e4e8}
.tool .url{margin-top:22px;font-size:13px;color:#e2e4e8}

/* team */
.team-title{left:0;top:2690px}
.team-sub{left:0;top:2790px;width:1200px;text-align:center;font-size:30px;color:var(--muted)}
.team-sub .serif{font-weight:400;color:var(--ink)}
.member{width:260px}
.member .photo{width:178px;height:178px;background:linear-gradient(160deg,#c9cdd2,#7a818b)}
.member .photo.lead{outline:5px solid var(--orange);outline-offset:-5px}
.member .name{margin-top:22px;font-size:21px;color:var(--ink)}
.member .role{font-size:14px;color:var(--muted)}

/* contact */
.contact{left:0;top:4172px;width:1200px;height:677px;background:linear-gradient(135deg,#14294a,var(--navy) 50%,#1b3459)}
.contact .section-title{color:var(--white);position:absolute;top:80px}
.contact .sub{position:absolute;top:150px;width:1200px;text-align:center;color:var(--white);font-size:26px;font-weight:300}
.field{position:absolute;background:var(--white);font-size:12px;color:#9aa0a8;padding:10px 12px}
.submit{position:absolute;left:259px;top:4780px}
.info{left:770px;top:4212px;color:var(--white);font-size:15px;line-height:1.95}
.footer-line{left:120px;top:4744px;width:960px;height:1px;background:rgba(255,255,255,.5)}
.copyright{left:0;top:4790px;width:1200px;text-align:center;color:var(--white);font-size:13px}
</style>
</head>
<body>

<section class="abs hero">
  <div class="abs hero-photo" role="img" aria-label="Hands holding a small green seedling in soft light"></div>
  <div class="abs brand">BRINDLE QUAY</div>
  <nav class="abs nav"><span class="active">ABOUT</span><span>SERVICES</span><span>TOOLS</span><span>TEAM</span><span>CONTACT</span></nav>
  <svg class="abs arrow" style="left:48px" width="24" height="44" viewBox="0 0 24 44"><path d="M20 4 L4 22 L20 40" fill="none" stroke="#fff" stroke-width="2.5"/></svg>
  <svg class="abs arrow" style="left:1128px" width="24" height="44" viewBox="0 0 24 44"><path d="M4 4 L20 22 L4 40" fill="none" stroke="#fff" stroke-width="2.5"/></svg>
  <div class="abs hero-title">
    <div class="serif">Agile</div>
    <div class="big">Consultancies</div>
    <div class="sub">FOR INTERNATIONAL DEVELOPMENT</div>
  </div>
  <span class="btn">Learn more &rsaquo;</span>
</section>

<section>
  <div class="abs about-photo" role="img" aria-label="Business team shaking hands around a meeting table"></div>
  <p class="abs about-text">Brindle Quay provides institutions working in the international cooperation field (implementing agencies, local governmental and non-governmental institutions) with solutions (hardware, software and consultancy services) to better organize, manage and exchange their knowledge in form of data and information (knowledge management).</p>
  <span class="abs btn about-btn">Learn more &rsaquo;</span>
</section>

<section class="abs agile">
  <div class="serif">Agile</div>
  <p>Efficient and flexible methodology for developing successful solutions with fun. Is is based on iterative, measurable and verifiable small steps, with integrative and empowering involvement of all actors.</p>
</section>

<h2 class="abs section-title services-title">SERVICES</h2>
<div class="abs service" style="left:109px">
  <div class="icon"><svg width="60" height="60" viewBox="0 0 60 60" fill="none" stroke="#fff" stroke-width="2.5"><circle cx="30" cy="30" r="6"/><path d="M30 24V10M30 36v14M24 30H10M36 30h14"/><circle cx="30" cy="8" r="3"/><circle cx="30" cy="52" r="3"/><circle cx="8" cy="30" r="3"/><circle cx="52" cy="30" r="3"/></svg></div>
  <h3>Technology for<br>International Aid</h3>
  <p>Meaningful implementation and application of Digital Media, Software and Hardware with a sensibility for the world.</p>
</div>
<div class="abs service" style="left:448px">
  <div class="icon"><svg width="60" height="60" viewBox="0 0 60 60" fill="none" stroke="#fff" stroke-width="2.5"><path d="M14 34h32l-4 18H18z"/><path d="M30 34V18"/><path d="M30 22c-8 0-12-6-12-12 8 0 12 6 12 12zM30 26c6 0 11-5 11-11-6 0-11 5-11 11z"/></svg></div>
  <h3>Organizational<br>Development</h3>
  <p>Agile and data-driven approach to accompany organizations into change processes.</p>
</div>
<div class="abs service" style="left:788px">
  <div class="icon"><svg width="60" height="60" viewBox="0 0 60 60" fill="none" stroke="#fff" stroke-width="2.5"><path d="M8 52h44"/><rect x="12" y="36" width="7" height="16"/><rect x="23" y="28" width="7" height="24"/><rect x="34" y="32" width="7" height="20"/><rect x="45" y="20" width="7" height="32"/><path d="M12 26l12-10 10 6 16-14M44 8h6v6"/></svg></div>
  <h3>Data &amp; Knowledge<br>Management</h3>
  <p>Needs assessment, organizational and requirement analysis for ICT-based support to knowledge processes in communities of practice.</p>
</div>

<section class="abs tools" role="img" aria-label="Blurred photo of people working in an office, darkened">
  <h2 class="section-title">OUR OPEN SOURCE TOOLS</h2>
</section>
<div class="abs tool" style="left:172px">
  <div class="head"><svg width="56" height="40" viewBox="0 0 56 40" fill="none" stroke="#f28a1b" stroke-width="2.5"><rect x="4" y="8" width="44" height="26" rx="4"/><path d="M4 16h44"/></svg>D-Vault</div>
  <p>Open Source web based document management system. The Software allows organizations and groups to flexibly manage their knowledge through documents and data. The files can be structured and access can be managed for groups of people or for specific persons.</p>
  <div class="url">https://code.example/brindlequay/d-vault</div>
</div>
<div class="abs tool" style="left:644px">
  <div class="head" style="margin-left:100px"><svg width="46" height="40" viewBox="0 0 46 40" fill="none" stroke="#f28a1b" stroke-width="2.5"><rect x="3" y="3" width="34" height="34"/><path d="M14 26l22-22M26 4h10v10"/></svg>D-Mesh</div>
  <p>Several decentralized D-Vaults can be connected over a D-Mesh. This allows to manage data over different instances and create organizational partnerships for networks of providing access to information and enhance knowledge in the developing world.</p>
  <div class="url">https://code.example/brindlequay/d-mesh</div>
</div>

<h2 class="abs section-title team-title">TEAM</h2>
<div class="abs team-sub">We are <span class="serif">cultural technologists</span></div>

<div class="abs member" style="left:162px;top:2975px"><div class="photo" role="img" aria-label="Portrait photo of team member"></div><div class="name">Dr. Marco Bellandi</div><div class="role">Chief Executive Officer</div></div>
<div class="abs member" style="left:470px;top:2975px"><div class="photo lead" role="img" aria-label="Portrait photo of team member"></div><div class="name">Irina Valtseva</div><div class="role">Chief Operations Officer</div></div>
<div class="abs member" style="left:776px;top:2975px"><div class="photo" role="img" aria-label="Portrait photo of team member"></div><div class="name">Jonas Marchetti</div><div class="role">Digital Product Manager</div></div>

<div class="abs member" style="left:162px;top:3370px"><div class="photo" role="img" aria-label="Portrait photo of team member"></div><div class="name">Luca Ferrandi</div><div class="role">Lead Developer</div></div>
<div class="abs member" style="left:470px;top:3370px"><div class="photo" role="img" aria-label="Portrait photo of team member"></div><div class="name">Timur Asanbekov</div><div class="role">Customer Liaison</div></div>
<div class="abs member" style="left:776px;top:3370px"><div class="photo" role="img" aria-label="Portrait photo of team member"></div><div class="name">Tobias Lindqvist</div><div class="role">Infrastructure Engineer</div></div>

<div class="abs member" style="left:162px;top:3765px"><div class="photo" role="img" aria-label="Portrait photo of team member"></div><div class="name">Rustam Oripov</div><div class="role">Sustainability Expert</div></div>
<div class="abs member" style="left:470px;top:3765px"><div class="photo" role="img" aria-label="Portrait photo of team member"></div><div class="name">Aliya Sharipova</div><div class="role">Customer Liaison</div></div>
<div class="abs member" style="left:776px;top:3765px"><div class="photo" role="img" aria-label="Portrait photo of team member"></div><div class="name">Davide Roncalli</div><div class="role">Search Engineer</div></div>

<section class="abs contact">
  <h2 class="section-title">CONTACT</h2>
  <div class="sub">Write and visit us</div>
</section>
<div class="field" style="left:259px;top:4382px;width:210px;height:38px">Name</div>
<div class="field" style="left:479px;top:4382px;width:210px;height:38px">Email</div>
<div class="field" style="left:259px;top:4430px;width:210px;height:38px">Phone No.</div>
<div class="field" style="left:479px;top:4430px;width:210px;height:38px">Subject</div>
<div class="field" style="left:259px;top:4478px;width:430px;height:120px">Message</div>
<span class="btn submit" style="top:4618px;font-size:14px;text-transform:none;padding:12px 22px">Submit &#10148;</span>
<svg class="abs" style="left:737px;top:4390px" width="16" height="22" viewBox="0 0 16 22" fill="none" stroke="#fff" stroke-width="1.8"><path d="M8 21s7-8 7-13A7 7 0 0 0 1 8c0 5 7 13 7 13z"/><circle cx="8" cy="8" r="2.5"/></svg>
<div class="abs info" style="top:4384px">Brindle Quay UG<br>Lindenhof Weg 14<br>10999 Berlin, Germany<br><span style="display:block;height:12px"></span>To be defined street<br>Karavan City, Kyrgyzstan<br><span style="display:block;height:12px"></span>Impressum</div>
<div class="abs footer-line"></div>
<div class="abs copyright">© Copyright 2017. Brindle Quay. All rights reserved.</div>

</body>
</html>
```